Dual (Twin) Wet Wipe Packaging

We are a NY Based Hygiene Brand Specifically for couples, Creating Dual products for Him and Her,
Brand Name is quelvin.
Our Initial Product is a single Wet wipe Dual Package with perforated lines one wipe for him and one for her used for after sex.
We Would like to see designs that show a bold modern design with slight edgy to bring out the fun!
The final design Should bring out the idea of couples, connection and bond,

Attached Are photos of color ideas And Attached Design ideas.

The measurement of each half should be 7*9 cm total 14*9 cm with both attached.

```html
<!DOCTYPE html>
<html lang="en">
<head>
<meta charset="utf-8">
<title>quelvin — dual wet wipe pack</title>
<link rel="stylesheet" href="https://fonts.googleapis.com/css2?family=Nunito:ital,wght@0,900;1,600&display=swap">
<style>
  :root {
    --page: #ffffff;
    --violet-deep: #8300f2;
    --violet-band: #911af7;
    --violet-pill: #8217e2;
    --mint-deep: #12dcc0;
    --mint-band: #12ebd0;
    --mint-pill: #10d6bc;
    --ink-light: #ffffff;
  }
  html, body {
    margin: 0;
    padding: 0;
    width: 1200px;
    height: 750px;
    overflow: hidden;
    background: var(--page);
  }
  .canvas {
    position: relative;
    width: 1200px;
    height: 750px;
  }
  .pack-art {
    position: absolute;
    inset: 0;
    width: 1200px;
    height: 750px;
  }
  .pack-label {
    position: absolute;
    left: 144px;
    width: 912px;
    top: 262px;
    height: 226px;
    display: flex;
    flex-direction: column;
    align-items: center;
    justify-content: center;
    color: var(--ink-light);
    text-align: center;
  }
  .brand-name {
    margin: 0;
    font-family: "Nunito", sans-serif;
    font-weight: 900;
    font-size: 150px;
    line-height: 1;
    letter-spacing: -2px;
    color: var(--ink-light);
    transform: translateY(-14px);
  }
  .tagline {
    margin: 0;
    width: 430px;
    font-family: "Nunito", sans-serif;
    font-style: italic;
    font-weight: 600;
    font-size: 16px;
    line-height: 23px;
    color: var(--ink-light);
  }
</style>
</head>
<body>
<main class="canvas">
  <svg class="pack-art" viewBox="0 0 1200 750" aria-hidden="true">
    <defs>
      <clipPath id="pack-shape">
        <rect x="144" y="82" width="912" height="586" rx="27" ry="27"/>
      </clipPath>
    </defs>
    <g clip-path="url(#pack-shape)">
      <rect class="half-his" x="144" y="82" width="456" height="586" fill="var(--violet-band)"/>
      <rect class="half-hers" x="600" y="82" width="456" height="586" fill="var(--mint-band)"/>
      <path class="corner-wave" fill="var(--violet-deep)" d="M144 82 H489 C470 160 400 200 298 223 C230 238 180 270 144 307 Z"/>
      <path class="corner-wave" fill="var(--violet-deep)" d="M144 668 H489 C470 590 400 550 298 527 C230 512 180 480 144 443 Z"/>
      <path class="corner-wave" fill="var(--mint-deep)" d="M1056 82 H711 C730 160 800 200 902 223 C970 238 1020 270 1056 307 Z"/>
      <path class="corner-wave" fill="var(--mint-deep)" d="M1056 668 H711 C730 590 800 550 902 527 C970 512 1020 480 1056 443 Z"/>
      <path class="label-pill-his" fill="var(--violet-pill)" d="M600 261 H299 A114 114 0 0 0 299 489 H600 Z"/>
      <path class="label-pill-hers" fill="var(--mint-pill)" d="M600 261 H890 A114 114 0 0 1 890 489 H600 Z"/>
    </g>
  </svg>

  <section class="pack-label">
    <h1 class="brand-name">quelvin</h1>
    <p class="tagline">A dual wet wipe designed for couples — one for you, one for your partner. Freshness after intimacy, wherever you are.</p>
  </section>
</main>
</body>
</html>
```